New modern business card design

To design a brand new business card that's clean & modern in terms of layout.
I have attached our company logo and also basic information regarding what is needed on the card that also needs to be editable.

Target Market(s)

motor trade

Contact Information for Business Card

logo, name, title, tel, mob, email, address, www, all information is in the word.doc file

Requirements
Must have
• white background
Nice to have
• Nice clean font

```html
<!DOCTYPE html>
<html lang="en">
<head>
<meta charset="utf-8">
<title>Brackley Auto Ltd – Business Card</title>
<link rel="stylesheet" href="https://fonts.googleapis.com/css2?family=Lato:wght@400;700&display=swap">
<style>
  :root {
    --brand-blue: #0b8cf0;
    --ink: #111111;
    --title-grey: #5a5a5a;
    --detail-grey: #444444;
    --paper: #ffffff;
  }
  * { margin: 0; padding: 0; box-sizing: border-box; }
  html, body {
    width: 1200px; height: 686px; overflow: hidden;
    background: var(--paper);
  }
  .card {
    position: relative;
    width: 1200px; height: 686px;
    background: var(--paper);
    font-family: 'Lato', sans-serif;
    overflow: hidden;
  }
  .brand {
    position: absolute;
    left: 100px; top: 304px;
    width: 410px;
    display: flex; align-items: center; justify-content: center; gap: 16px;
  }
  .brand-square {
    width: 32px; height: 32px;
    background: var(--brand-blue);
    flex: none;
  }
  .brand-name {
    font-weight: 700;
    font-size: 38px;
    letter-spacing: 1px;
    color: var(--ink);
    white-space: nowrap;
  }
  .divider {
    position: absolute;
    left: 588px; top: 127px;
    width: 4px; height: 473px;
    background: var(--brand-blue);
  }
  .person {
    position: absolute;
    left: 619px; top: 117px;
  }
  .person-name {
    font-size: 70px;
    line-height: 1;
    color: var(--ink);
    font-weight: 400;
    white-space: nowrap;
  }
  .person-name .first { color: var(--brand-blue); font-weight: 700; }
  .person-title {
    margin-top: 12px;
    font-size: 46px;
    line-height: 1;
    letter-spacing: 7.6px;
    color: var(--title-grey);
    white-space: nowrap;
  }
  .contacts {
    position: absolute;
    left: 623px; top: 302px;
    list-style: none;
  }
  .contact {
    display: flex; align-items: center;
    height: 46px;
    margin-bottom: 11px;
  }
  .contact-icon {
    width: 46px; height: 46px; flex: none;
  }
  .contact-text {
    margin-left: 40px;
    font-size: 25px;
    line-height: 32px;
    color: var(--detail-grey);
    white-space: nowrap;
  }
  .contact.address .contact-text { margin-top: 22px; }
  .footer-band {
    position: absolute;
    left: 0; bottom: 0;
    width: 1200px; height: 13px;
    background: var(--brand-blue);
  }
</style>
</head>
<body>
<div class="card">
  <div class="brand">
    <span class="brand-square"></span>
    <span class="brand-name">BRACKLEY AUTO LTD</span>
  </div>

  <div class="divider"></div>

  <div class="person">
    <h1 class="person-name"><span class="first">Daniel</span> Hartley</h1>
    <p class="person-title">General Manager</p>
  </div>

  <ul class="contacts">
    <li class="contact mobile">
      <svg class="contact-icon" viewBox="0 0 46 46" aria-hidden="true">
        <circle cx="23" cy="23" r="23" fill="var(--brand-blue)"/>
        <rect x="16.5" y="10" width="13" height="26" rx="2" fill="none" stroke="#fff" stroke-width="2"/>
        <line x1="20.5" y1="13.5" x2="25.5" y2="13.5" stroke="#fff" stroke-width="1.5"/>
        <circle cx="23" cy="32" r="1.4" fill="#fff"/>
      </svg>
      <span class="contact-text">07412 638 519</span>
    </li>
    <li class="contact landline">
      <svg class="contact-icon" viewBox="0 0 46 46" aria-hidden="true">
        <circle cx="23" cy="23" r="23" fill="var(--brand-blue)"/>
        <path d="M9 19 Q23 9 37 19 L34 23 L29 21 L29 18 Q23 16 17 18 L17 21 L12 23 Z" fill="#fff"/>
        <path d="M14 34 L17 23 L29 23 L32 34 Z" fill="#fff"/>
        <circle cx="23" cy="29" r="3.2" fill="var(--brand-blue)"/>
      </svg>
      <span class="contact-text">0161 482 9071</span>
    </li>
    <li class="contact email">
      <svg class="contact-icon" viewBox="0 0 46 46" aria-hidden="true">
        <circle cx="23" cy="23" r="23" fill="var(--brand-blue)"/>
        <rect x="11" y="14" width="24" height="18" rx="1.5" fill="#fff"/>
        <path d="M11.5 15 L23 25 L34.5 15" fill="none" stroke="var(--brand-blue)" stroke-width="2"/>
      </svg>
      <span class="contact-text">dhartley@brackley-auto.co.uk</span>
    </li>
    <li class="contact web">
      <svg class="contact-icon" viewBox="0 0 46 46" aria-hidden="true">
        <circle cx="23" cy="23" r="23" fill="var(--brand-blue)"/>
        <g fill="none" stroke="#fff" stroke-width="1.8">
          <circle cx="23" cy="23" r="12"/>
          <ellipse cx="23" cy="23" rx="5.5" ry="12"/>
          <line x1="23" y1="11" x2="23" y2="35"/>
          <line x1="11" y1="23" x2="35" y2="23"/>
          <path d="M13 16.5 H33 M13 29.5 H33"/>
        </g>
      </svg>
      <span class="contact-text">www.brackley-auto.co.uk</span>
    </li>
    <li class="contact address">
      <svg class="contact-icon" viewBox="0 0 46 46" aria-hidden="true">
        <circle cx="23" cy="23" r="23" fill="var(--brand-blue)"/>
        <path d="M23 36 C17 28 14 24 14 19 A9 9 0 0 1 32 19 C32 24 29 28 23 36 Z" fill="#fff"/>
        <circle cx="23" cy="19" r="3.5" fill="var(--brand-blue)"/>
      </svg>
      <span class="contact-text">Harwood Street / Denford,<br>Manchester / M21 4QT</span>
    </li>
  </ul>

  <div class="footer-band"></div>
</div>
</body>
</html>
```